Generative AI radar Infographics

I want to create an infographic called "Machine Learning Prospect Compass for Tender Replies". (see slide 3 of the PowerPoint file). I want to use it on social media (ConnectHub and Website). I added 2 inspiration graphics in my brief (see slide 2 of the PowerPoint). I want to add my logo on the infographic. (I also uploaded my company logos). You can find model detailed instructions on slide 1 of the PowerPoint.
Business development and sales
I am a business consultant. I will be using this infographics on Connecthub and in my powerpoint presentations to clients

```html
<!DOCTYPE html>
<html lang="en">
<head>
<meta charset="utf-8">
<title>Machine Learning Prospect Compass for Tender Replies</title>
<link rel="stylesheet" href="https://fonts.googleapis.com/css2?family=Montserrat:wght@500;600;700;800&display=swap">
<style>
  :root {
    --ink: #0b2d40;
    --text: #1b1b1b;
    --band: #0a2d40;
    --white: #ffffff;
    --tl-outer: #8797a1;
    --tl-inner: #647985;
    --tr-outer: #85c7da;
    --tr-inner: #45aacb;
    --bl-outer: #bfc8cd;
    --bl-inner: #98a5ab;
    --br-outer: #bdeaf9;
    --br-inner: #7fe0f5;
  }
  * { margin: 0; padding: 0; box-sizing: border-box; }
  html, body { width: 1200px; height: 1000px; overflow: hidden; background: var(--white); }
  .infographic {
    position: relative;
    width: 1200px;
    height: 1000px;
    font-family: "Montserrat", Arial, sans-serif;
    color: var(--text);
  }
  .title {
    position: absolute;
    left: 70px;
    top: 70px;
    font-size: 60px;
    line-height: 72px;
    font-weight: 800;
    color: var(--ink);
    letter-spacing: -0.3px;
    white-space: nowrap;
  }
  .title-line { display: block; }
  .footer-band {
    position: absolute;
    left: 0;
    top: 805px;
    width: 1200px;
    height: 175px;
    background: var(--band);
  }
  .radar {
    position: absolute;
    left: 0;
    top: 0;
  }
  .axis-label { font-size: 17px; font-weight: 700; fill: var(--text); }
  .axis-label--light { fill: var(--white); }
  .axis-note { font-size: 12px; font-weight: 700; fill: var(--text); }
  .quadrant-label { font-size: 26px; font-weight: 700; fill: #111; }
  .item { font-size: 15px; font-weight: 500; fill: var(--text); }
  .divider { stroke: rgba(255,255,255,0.55); stroke-width: 1; }
  .brand {
    position: absolute;
    left: 82px;
    top: 852px;
    display: flex;
    align-items: center;
    gap: 14px;
    color: var(--white);
    font-weight: 600;
  }
  .brand-mark {
    width: 16px;
    height: 16px;
    border-radius: 50%;
    background: var(--white);
  }
  .brand-name { line-height: 1; }
  .brand-name .primary { display: block; font-size: 40px; letter-spacing: 2px; }
  .brand-name .secondary { display: block; font-size: 15px; letter-spacing: 4px; margin-top: 8px; }
</style>
</head>
<body>
<main class="infographic">
  <h1 class="title"><span class="title-line">Machine Learning Prospect</span><span class="title-line">Compass for Tender Replies</span></h1>

  <div class="footer-band"></div>

  <svg class="radar" width="1200" height="1000" viewBox="0 0 1200 1000" aria-label="Compass of machine learning opportunities in four quadrants">
    <defs>
      <path id="arc-decision" d="M397 565 A250 250 0 0 1 647 315"/>
      <path id="arc-development" d="M647 315 A250 250 0 0 1 897 565"/>
      <path id="arc-capture" d="M357 565 A290 290 0 0 0 647 855"/>
      <path id="arc-strategy" d="M647 855 A290 290 0 0 0 937 565"/>
    </defs>

    <path d="M647 565 L322 565 A325 325 0 0 1 647 240 Z" fill="var(--tl-outer)"/>
    <path d="M647 565 L647 240 A325 325 0 0 1 972 565 Z" fill="var(--tr-outer)"/>
    <path d="M647 565 L972 565 A325 325 0 0 1 647 890 Z" fill="var(--br-outer)"/>
    <path d="M647 565 L647 890 A325 325 0 0 1 322 565 Z" fill="var(--bl-outer)"/>

    <path d="M647 565 L434 565 A213 213 0 0 1 647 352 Z" fill="var(--tl-inner)"/>
    <path d="M647 565 L647 352 A213 213 0 0 1 860 565 Z" fill="var(--tr-inner)"/>
    <path d="M647 565 L860 565 A213 213 0 0 1 647 778 Z" fill="var(--br-inner)"/>
    <path d="M647 565 L647 778 A213 213 0 0 1 434 565 Z" fill="var(--bl-inner)"/>

    <circle cx="647" cy="565" r="92" fill="rgba(0,0,0,0.045)"/>
    <line class="divider" x1="647" y1="240" x2="647" y2="890"/>

    <text class="quadrant-label"><textPath href="#arc-decision" startOffset="50%" text-anchor="middle">Decision Support</textPath></text>
    <text class="quadrant-label"><textPath href="#arc-development" startOffset="50%" text-anchor="middle">Proposal Development</textPath></text>
    <text class="quadrant-label"><textPath href="#arc-capture" startOffset="50%" text-anchor="middle">Capture Strategy</textPath></text>
    <text class="quadrant-label"><textPath href="#arc-strategy" startOffset="50%" text-anchor="middle">Proposal Strategy</textPath></text>

    <text class="axis-label" x="647" y="233" text-anchor="middle">Process Enhancement</text>
    <text class="axis-label" x="317" y="560" text-anchor="end">Insights Generation</text>
    <text class="axis-note" x="317" y="580" text-anchor="end">(Transformative Application)</text>
    <text class="axis-label" x="975" y="560">Task Automation</text>
    <text class="axis-note" x="975" y="580">(Foundational Use)</text>
    <text class="axis-label axis-label--light" x="647" y="913" text-anchor="middle">Strategy Enablement</text>

    <g class="items items--decision" text-anchor="end">
      <text class="item" x="643" y="430">Bid/No Bid Analysis</text>
      <text class="item" x="643" y="455">Bid Qualification</text>
      <text class="item" x="643" y="480">Opportunity Assessment</text>
      <text class="item" x="643" y="505">Win Probability Modeling</text>
      <text class="item" x="643" y="530">Strategic Pricing Optimization</text>
      <text class="item" x="643" y="556">Compliance Assessment</text>
    </g>

    <g class="items items--development">
      <text class="item" x="655" y="382">Company profile</text>
      <text class="item" x="655" y="404">CV and Resumes</text>
      <text class="item" x="655" y="426">Past Performance</text>
      <text class="item" x="655" y="448">Technical Solution</text>
      <text class="item" x="655" y="470">Compliance Matrix</text>
      <text class="item" x="655" y="492">Statement of Work</text>
      <text class="item" x="655" y="514">Executive Summary</text>
      <text class="item" x="655" y="536">Security Questionnaires</text>
      <text class="item" x="655" y="558">Due Diligence Questionnaires</text>
    </g>

    <g class="items items--capture" text-anchor="end">
      <text class="item" x="639" y="586">Capture Plan</text>
      <text class="item" x="639" y="608">SWOT Analysis</text>
      <text class="item" x="639" y="630">Customer Hot Buttons</text>
      <text class="item" x="639" y="652">Customer Intelligence</text>
      <text class="item" x="639" y="674">Competitive Intelligence</text>
      <text class="item" x="639" y="696">Value Proposition</text>
    </g>

    <g class="items items--strategy">
      <text class="item" x="655" y="586">Proposal Plan</text>
      <text class="item" x="655" y="608">Proposal Outline</text>
      <text class="item" x="655" y="630">Differentiators</text>
      <text class="item" x="655" y="652">Win Theme Extraction</text>
      <text class="item" x="655" y="674">Key Messages Extraction</text>
    </g>
  </svg>

  <div class="brand">
    <span class="brand-mark"></span>
    <span class="brand-name">
      <span class="primary">HALVORNE</span>
      <span class="secondary">ADVISORY GROUP</span>
    </span>
  </div>
</main>
</body>
</html>
```